*** Business Card Design Project

I need a logo and business card for my new catering business: "Brevano". The design should be modern, clean, elegant and refined. One or Two colours only. The design SHOULD NOT include graphics or images. There should be space for my name, phone number and email address (I will provide these to you later).

Industry/Entity Type

Catering

Requirements
Must have
• Must have one or two colours only.
Must include the text "brevano"
Should not have
• Must not have graphics or images.

```html
<!DOCTYPE html>
<html lang="en">
<head>
<meta charset="utf-8">
<title>Brevano Business Card</title>
<link rel="stylesheet" href="https://fonts.googleapis.com/css2?family=Source+Sans+3:wght@400;600&display=swap">
<style>
  :root {
    --backdrop: #6f6f6f;
    --card-black: #1d1d1d;
    --card-white: #f4f4f2;
    --brand-red: #8f1c20;
    --ink: #1b1b1b;
    --ink-soft: #3a3a3a;
    --muted-light: #d6d6d6;
  }
  * { margin: 0; padding: 0; box-sizing: border-box; }
  html, body {
    width: 1200px;
    height: 880px;
    overflow: hidden;
    background: var(--backdrop);
    font-family: "Source Sans 3", sans-serif;
  }
  .canvas {
    width: 1200px;
    height: 880px;
    display: flex;
    align-items: center;
    justify-content: center;
    gap: 60px;
  }
  .card {
    width: 520px;
    height: 297px;
    position: relative;
    box-shadow: 0 12px 30px rgba(0,0,0,0.35);
  }

  /* Back side */
  .card-back {
    background: var(--card-black);
    display: flex;
    flex-direction: column;
    align-items: center;
    justify-content: center;
  }
  .brand-name {
    font-weight: 400;
    font-size: 46px;
    letter-spacing: 2px;
    color: var(--brand-red);
    line-height: 1;
  }
  .back-url {
    margin-top: 40px;
    font-size: 14px;
    color: var(--muted-light);
  }

  /* Front side */
  .card-front {
    background: var(--card-white);
    padding: 30px 34px;
  }
  .card-front .brand-name {
    font-size: 38px;
  }
  .contact-block {
    position: absolute;
    left: 34px;
    top: 120px;
    display: grid;
    grid-template-columns: auto auto;
    column-gap: 26px;
    row-gap: 3px;
    font-size: 13.5px;
    color: var(--ink);
  }
  .contact-label {
    color: var(--brand-red);
  }
  .holder {
    position: absolute;
    right: 34px;
    bottom: 30px;
    text-align: right;
  }
  .holder-name {
    font-weight: 600;
    font-size: 22px;
    color: var(--brand-red);
  }
  .holder-title {
    font-size: 13px;
    color: var(--ink-soft);
  }
</style>
</head>
<body>
<main class="canvas">
  <section class="card card-back" aria-label="Business card back">
    <p class="brand-name">Brevano</p>
    <p class="back-url">www.brevano.com</p>
  </section>

  <section class="card card-front" aria-label="Business card front">
    <p class="brand-name">Brevano</p>
    <div class="contact-block">
      <p><span class="contact-label">Phone:</span> +1 555-310-4821</p>
      <p><span class="contact-label">Fax:</span> +1 555-310-4822</p>
      <p><span class="contact-label">Mobile:</span> +1 555-672-9035</p>
      <p><span class="contact-label">Email:</span> marcus@brevano.com</p>
      <p><span class="contact-label">Website:</span> www.brevano.com</p>
    </div>
    <div class="holder">
      <p class="holder-name">Marcus Ellwood</p>
      <p class="holder-title">Managing Director</p>
    </div>
  </section>
</main>
</body>
</html>
```